Real Estate Seller Leads Ad

I want a creative ad to run on social media. Need the ad to be created with correct sizing for facebook, instagram, twitter and pintrest and our website lead form page [login to view URL] This ad is to be designed for social media to generate real estate seller leads. I have attached some examples for you to look over. I have also included our logo. Brindlecove Real Estate Logo. This is our website [login to view URL] This is the lead [login to view URL] website [login to view URL] To clarify I want the ad to be designed to post on social media advertising section and the ad creation for our lead form on our website. Please review our website lead form page to make appropriate images to size.

```html
<!DOCTYPE html>
<html lang="en">
<head>
<meta charset="utf-8">
<title>Brindlecove Real Estate – Seller Leads Ad</title>
<link rel="stylesheet" href="https://fonts.googleapis.com/css2?family=Bebas+Neue&family=Oswald:wght@500;600&family=Open+Sans:wght@400;600&display=swap">
<style>
  :root {
    --page: #ffffff;
    --ink: #3a3b40;
    --band: rgba(62, 62, 68, 0.9);
    --panel: rgba(238, 242, 238, 0.78);
    --accent: #e2502a;
    --light: #ffffff;
    --label: #222222;
    --sky: #9cc6ee;
    --houses: #7f8f86;
    --foliage: #8fae4c;
    --lawn: #5c9a2a;
  }
  * { margin: 0; padding: 0; box-sizing: border-box; }
  html, body { width: 1027px; height: 1200px; overflow: hidden; background: var(--page); }
  body { position: relative; font-family: "Open Sans", Arial, sans-serif; }

  .ad { position: absolute; overflow: hidden; box-shadow: 3px 4px 7px rgba(0,0,0,0.35); }
  .ad--cover { left: 129px; top: 105px; width: 769px; height: 285px; }
  .ad--banner { left: 144px; top: 511px; width: 726px; height: 541px; }

  .ad__photo {
    position: absolute; inset: 0;
    background:
      radial-gradient(ellipse 32% 38% at 62% 12%, rgba(156,198,238,0.95) 0%, rgba(156,198,238,0) 100%),
      radial-gradient(ellipse 30% 55% at 90% 35%, rgba(150,160,90,0.8) 0%, rgba(150,160,90,0) 100%),
      radial-gradient(ellipse 55% 45% at 22% 38%, rgba(112,128,122,0.9) 0%, rgba(112,128,122,0) 100%),
      radial-gradient(ellipse 40% 30% at 45% 42%, rgba(70,98,140,0.55) 0%, rgba(70,98,140,0) 100%),
      linear-gradient(180deg, #b9cfd6 0%, var(--foliage) 45%, var(--lawn) 72%, #4f8a26 100%);
  }

  .brand-band { position: absolute; left: 0; top: 0; background: var(--band); display: flex; align-items: center; }
  .ad--cover .brand-band { width: 342px; height: 66px; clip-path: polygon(0 0, 100% 0, 87% 100%, 0 100%); padding-left: 26px; gap: 10px; }
  .ad--banner .brand-band { width: 358px; height: 92px; clip-path: polygon(0 0, 100% 0, 89% 100%, 0 100%); padding-left: 28px; gap: 12px; }

  .brand-mark { background: var(--accent); flex: none; }
  .ad--cover .brand-mark { width: 34px; height: 34px; }
  .ad--banner .brand-mark { width: 40px; height: 40px; }

  .brand-name { color: var(--light); font-family: "Open Sans", Arial, sans-serif; font-weight: 400; line-height: 1; }
  .brand-name span { display: block; }
  .brand-name .brand-tag { letter-spacing: 4px; margin-top: 4px; }
  .ad--cover .brand-name { font-size: 26px; }
  .ad--cover .brand-tag { font-size: 11px; }
  .ad--banner .brand-name { font-size: 30px; }
  .ad--banner .brand-tag { font-size: 12px; }

  .url-band { position: absolute; top: 0; right: 0; background: var(--band); color: var(--light); display: flex; align-items: center; gap: 12px; font-weight: 400; }
  .ad--cover .url-band { width: 396px; height: 57px; clip-path: polygon(4.3% 0, 100% 0, 100% 100%, 0 100%); padding-left: 34px; font-size: 24px; }
  .ad--banner .url-band { width: 374px; height: 52px; clip-path: polygon(3.8% 0, 100% 0, 100% 100%, 0 100%); padding-left: 28px; font-size: 23px; }
  .url-band svg { flex: none; }

  .pitch { position: absolute; background: var(--panel); color: var(--ink); }
  .ad--cover .pitch { left: 333px; top: 172px; width: 436px; height: 100px; clip-path: polygon(0 0, 100% 0, 100% 100%, 6% 100%); text-align: right; padding: 16px 20px 0 0; }
  .ad--banner .pitch { left: 0; top: 321px; width: 641px; height: 147px; clip-path: polygon(0 0, 100% 0, 89.7% 100%, 0 100%); padding: 20px 0 0 35px; }

  .pitch__headline { font-family: "Bebas Neue", "Oswald", sans-serif; font-weight: 400; line-height: 1; letter-spacing: 0.5px; }
  .ad--cover .pitch__headline { font-size: 53px; }
  .ad--banner .pitch__headline { font-size: 79px; }

  .pitch__offer { font-family: "Oswald", Arial, sans-serif; font-weight: 500; text-transform: uppercase; letter-spacing: 0.6px; line-height: 1; }
  .ad--cover .pitch__offer { font-size: 15.5px; margin-top: 6px; }
  .ad--banner .pitch__offer { font-size: 21px; margin-top: 6px; }

  .format-label { position: absolute; display: flex; align-items: center; font-family: "Open Sans", Arial, sans-serif; font-size: 20px; letter-spacing: 1px; color: var(--label); }
  .format-label::before { content: ""; display: block; height: 1.5px; background: var(--label); margin-right: 18px; }
  .format-label--cover { left: 129px; top: 408px; }
  .format-label--cover::before { width: 318px; }
  .format-label--banner { left: 144px; top: 1074px; }
  .format-label--banner::before { width: 320px; }
</style>
</head>
<body>

  <section class="ad ad--cover">
    <div class="ad__photo" role="img" aria-label="Sunny residential street of porched clapboard houses with green lawns, shrubs and a leafy tree"></div>
    <div class="brand-band">
      <div class="brand-mark"></div>
      <div class="brand-name"><span>Brindlecove</span><span class="brand-tag">REAL ESTATE</span></div>
    </div>
    <div class="url-band">
      <svg width="26" height="26" viewBox="0 0 26 26" fill="none" stroke="#ffffff" stroke-width="1.8" aria-hidden="true">
        <circle cx="13" cy="13" r="11"/><ellipse cx="13" cy="13" rx="5" ry="11"/><line x1="2" y1="13" x2="24" y2="13"/><path d="M4 7.5h18M4 18.5h18"/>
      </svg>
      <span>www.brindlecove.com</span>
    </div>
    <div class="pitch">
      <h2 class="pitch__headline">IS IT TIME TO SELL ?</h2>
      <p class="pitch__offer">Find out now with a free home value report.</p>
    </div>
  </section>
  <p class="format-label format-label--cover">COVER PHOTO</p>

  <section class="ad ad--banner">
    <div class="ad__photo" role="img" aria-label="Sunny residential street of porched clapboard houses with green lawns, a curving footpath and a leafy tree"></div>
    <div class="brand-band">
      <div class="brand-mark"></div>
      <div class="brand-name"><span>Brindlecove</span><span class="brand-tag">REAL ESTATE</span></div>
    </div>
    <div class="url-band">
      <svg width="26" height="26" viewBox="0 0 26 26" fill="none" stroke="#ffffff" stroke-width="1.8" aria-hidden="true">
        <circle cx="13" cy="13" r="11"/><ellipse cx="13" cy="13" rx="5" ry="11"/><line x1="2" y1="13" x2="24" y2="13"/><path d="M4 7.5h18M4 18.5h18"/>
      </svg>
      <span>www.brindlecove.com</span>
    </div>
    <div class="pitch">
      <h2 class="pitch__headline">IS IT TIME TO SELL ?</h2>
      <p class="pitch__offer">Find out now with a free home value report.</p>
    </div>
  </section>
  <p class="format-label format-label--banner">BANNER FOR AD</p>

</body>
</html>
```